La etiqueta deberá contener lo siguiente:
-Titulo: Miel de Agave Kosher
-Logo de DOVRA (realizado por ustedes, adjunto diseño)
-Logo del certificado: KOSHER (Se adjuntan certificado)
-Mililitros: 750 ml
-Información nutrimental: se adjunta tabla
La miel deberá sobresalir de las demás por el estilo lujoso y llamativo de la etiqueta.

```html
<!DOCTYPE html>
<html lang="es">
<head>
<meta charset="utf-8">
<title>Miel de Agave Kosher – Etiqueta</title>
<link rel="stylesheet" href="https://fonts.googleapis.com/css2?family=Montserrat:wght@300;400;600&display=swap">
<style>
  :root {
    --page-bg: #ffffff;
    --label-base: #3b3c3f;
    --label-edge: #2c2d30;
    --label-light: #4a4b4e;
    --ink-light: #f2f2f2;
    --ink-soft: #d9d9d9;
    --gold: #c8a55a;
    --gold-deep: #9c7a32;
    --agave-tone: #55575b;
  }
  html, body {
    margin: 0;
    padding: 0;
    width: 1200px;
    height: 1200px;
    overflow: hidden;
    background: var(--page-bg);
  }
  .canvas {
    position: relative;
    width: 1200px;
    height: 1200px;
  }
  .label {
    position: absolute;
    left: 300px;
    top: 150px;
    width: 600px;
    height: 900px;
    background: linear-gradient(90deg, var(--label-edge) 0%, var(--label-base) 18%, var(--label-light) 50%, var(--label-base) 82%, var(--label-edge) 100%);
    font-family: "Montserrat", sans-serif;
    color: var(--ink-light);
    text-align: center;
  }
  .cert-seal {
    position: absolute;
    left: 347px;
    top: 47px;
    width: 110px;
    height: 110px;
  }
  .product-title {
    position: absolute;
    left: 0;
    right: 0;
    top: 198px;
    margin: 0;
    font-weight: 600;
    font-size: 58px;
    line-height: 77px;
    letter-spacing: 0.09em;
    text-transform: uppercase;
  }
  .product-variant {
    position: absolute;
    left: 0;
    right: 0;
    top: 385px;
    margin: 0;
    font-weight: 300;
    font-size: 27px;
    letter-spacing: 0.06em;
    color: var(--ink-soft);
  }
  .agave-backdrop {
    position: absolute;
    left: 115px;
    top: 560px;
    width: 370px;
    height: 175px;
    background: radial-gradient(ellipse at 50% 60%, var(--agave-tone) 0%, rgba(85,87,91,0) 70%);
  }
  .brand-dot {
    position: absolute;
    left: 255px;
    top: 520px;
    width: 84px;
    height: 84px;
    border: 5px solid var(--gold);
    border-radius: 50%;
    box-sizing: border-box;
  }
  .brand-name {
    position: absolute;
    left: 0;
    right: 0;
    top: 652px;
    margin: 0;
    font-weight: 400;
    font-size: 64px;
    line-height: 1;
    letter-spacing: 0.16em;
    padding-left: 0.16em;
  }
  .gold-rule {
    position: absolute;
    left: 223px;
    top: 781px;
    width: 148px;
    height: 5px;
    background: var(--gold);
  }
  .volume {
    position: absolute;
    left: 0;
    right: 0;
    top: 810px;
    margin: 0;
    font-weight: 300;
    font-size: 25px;
    letter-spacing: 0.04em;
    color: var(--ink-soft);
  }
  .volume .unit {
    font-size: 18px;
  }
</style>
</head>
<body>
<main class="canvas">
  <section class="label">
    <svg class="cert-seal" viewBox="0 0 110 110" role="img" aria-label="Sello de certificación kosher">
      <circle cx="55" cy="55" r="53" fill="var(--gold-deep)"/>
      <circle cx="55" cy="55" r="46" fill="none" stroke="var(--gold)" stroke-width="4"/>
      <circle cx="55" cy="55" r="30" fill="var(--gold)"/>
    </svg>

    <h1 class="product-title">Miel de<br>Agave</h1>
    <p class="product-variant">KOSHER</p>

    <div class="agave-backdrop" role="img" aria-label="Planta de agave tenue de fondo"></div>
    <div class="brand-dot"></div>
    <p class="brand-name">DOVRA</p>

    <div class="gold-rule"></div>
    <p class="volume">750 <span class="unit">ML</span></p>
  </section>
</main>
</body>
</html>
```